Circus Poster 2016

We want to revise our circus poster for our 2016 tour. We very much liked the poster we used last year (attached) and want to stay with this colour scheme and with this logo. However, we want to enhance the family friendliness of the poster, so perhaps the addition of a family having a great time would be a good idea.

The winner will be paid to modify this poster for each of the 30 events we are doing this year plus making a flyer (based on the poster design). So the winner of this contest gets a job for a year.

Circus

```html
<!DOCTYPE html>
<html lang="en">
<head>
<meta charset="utf-8">
<title>Marvello's Circus – Ashbury, Willowmere Park</title>
<link href="https://fonts.googleapis.com/css2?family=PT+Sans+Narrow:wght@700&display=swap" rel="stylesheet">
<style>
  :root{
    --bg-deep:#2a1c22;
    --bg-red:#7a1020;
    --bg-green:#2f4a2a;
    --bg-slate:#2c3340;
    --title-red:#e8443f;
    --rule-teal:#1fa39c;
    --ink-white:#ffffff;
    --ink-lilac:#c9bcd6;
    --ink-pink:#f0a0a6;
    --ink-mint:#a8e6e0;
    --ink-yellow:#fff08a;
    --art-red:#d8323f;
    --art-teal:#3bb3aa;
    --art-gold:#cfae6a;
    --art-maroon:#6e1a2a;
    --beam-teal:rgba(40,170,160,.45);
    --beam-red:rgba(220,40,40,.45);
    --beam-yellow:rgba(220,210,40,.45);
    --lamp:#1c1c1e;
  }
  *{margin:0;padding:0;box-sizing:border-box}
  html,body{width:776px;height:1200px;overflow:hidden;background:var(--bg-deep)}
  .poster{
    position:relative;width:776px;height:1200px;overflow:hidden;
    font-family:"PT Sans Narrow",Arial,sans-serif;font-weight:700;
    background:
      radial-gradient(ellipse 60% 45% at 0% 0%,var(--bg-red),transparent 70%),
      radial-gradient(ellipse 55% 45% at 100% 10%,var(--bg-green),transparent 70%),
      radial-gradient(ellipse 70% 50% at 50% 100%,#4a2418,transparent 70%),
      linear-gradient(180deg,#3a1c26 0%,var(--bg-slate) 45%,#2a2022 100%);
  }
  .beams{position:absolute;inset:0;width:776px;height:1200px}

  .brand{
    position:absolute;left:0;right:0;top:12px;text-align:center;
    color:var(--title-red);text-transform:uppercase;line-height:1;
  }
  .brand__owner{display:block;font-size:60px;letter-spacing:3px}
  .brand__word{display:block;font-size:168px;letter-spacing:20px;margin-top:-14px;padding-left:20px}

  .show-art{
    position:absolute;left:83px;top:200px;width:597px;height:570px;border-radius:50%;
    background:
      radial-gradient(ellipse 45% 50% at 50% 58%,var(--art-red) 0%,var(--art-teal) 55%,transparent 80%),
      radial-gradient(circle at 50% 50%,var(--art-gold) 0%,var(--art-maroon) 100%);
  }

  .venue{position:absolute;left:0;right:0;text-align:center;line-height:1;text-transform:uppercase;white-space:nowrap}
  .text-spectrum{
    background:linear-gradient(90deg,var(--ink-white) 0%,var(--ink-mint) 20%,var(--ink-lilac) 40%,var(--ink-pink) 62%,var(--ink-yellow) 85%,var(--ink-white) 100%);
    -webkit-background-clip:text;background-clip:text;color:transparent;
  }
  .venue--town{top:760px;font-size:116px}
  .venue--park{top:858px;font-size:108px}

  .rule{position:absolute;height:3px;background:var(--rule-teal)}
  .rule--under-town{left:40px;width:712px;top:868px}
  .rule--under-park{left:18px;width:740px;top:960px}
  .rule--under-details{left:18px;width:722px;top:1116px}
  .rule--v{width:3px}
  .rule--details{left:448px;top:963px;height:153px}
  .rule--contact{left:486px;top:1122px;height:36px}

  .details{position:absolute;text-transform:uppercase;text-align:center;font-size:64px;line-height:80px;white-space:nowrap}
  .details--address{left:18px;width:426px;top:958px}
  .details--dates{left:452px;width:290px;top:958px}

  .contact{position:absolute;top:1120px;font-size:38px;line-height:42px;text-transform:uppercase;white-space:nowrap}
  .contact--web{left:22px}
  .contact--phone{left:506px}

  .stage-lamps{position:absolute;left:0;right:0;bottom:0;height:44px}
</style>
</head>
<body>
<main class="poster">
  <svg class="beams" viewBox="0 0 776 1200" aria-hidden="true">
    <defs>
      <filter id="soft"><feGaussianBlur stdDeviation="14"/></filter>
    </defs>
    <g filter="url(#soft)">
      <polygon points="0,560 110,540 140,1200 40,1200" fill="var(--beam-teal)"/>
      <polygon points="300,900 430,880 520,1200 330,1200" fill="var(--beam-red)"/>
      <polygon points="700,560 776,540 776,760 640,1200 560,1200" fill="var(--beam-yellow)"/>
    </g>
  </svg>

  <div class="show-art" role="img" aria-label="Illustration area: red and teal striped big top tent in front of a gold and maroon sunburst, with a small elephant balancing on a ball in the entrance"></div>

  <h1 class="brand">
    <span class="brand__owner">Marvello's</span>
    <span class="brand__word">Circus</span>
  </h1>

  <p class="venue venue--town text-spectrum">Ashbury</p>
  <div class="rule rule--under-town"></div>
  <p class="venue venue--park text-spectrum">Willowmere Park</p>
  <div class="rule rule--under-park"></div>

  <p class="details details--address text-spectrum">Fenwick<br>Road, HX99 1ZZ</p>
  <div class="rule rule--v rule--details"></div>
  <p class="details details--dates text-spectrum">9-12 July<br>2015</p>

  <div class="rule rule--under-details"></div>
  <p class="contact contact--web text-spectrum">www.marvelloscircus.com</p>
  <div class="rule rule--v rule--contact"></div>
  <p class="contact contact--phone text-spectrum">01632 555 250</p>

  <svg class="stage-lamps" viewBox="0 0 776 44" aria-hidden="true">
    <rect x="60" y="14" width="36" height="30" rx="6" fill="var(--lamp)"/>
    <rect x="275" y="14" width="36" height="30" rx="6" fill="var(--lamp)"/>
    <rect x="460" y="14" width="36" height="30" rx="6" fill="var(--lamp)"/>
    <rect x="672" y="14" width="36" height="30" rx="6" fill="var(--lamp)"/>
  </svg>
</main>
</body>
</html>
```